ONE PAGE WEB DESIGN NEEDED for Finance Company

We need a web design (ONE PAGE DESIGN ONLY) for a new finance website called Brightwell Lending. Brightwell Lending helps customers get the right loan, whether its a home loan, investment loan, business loan etc.

You are required to come up with just the homepage design. Professionalism and quality is the key factors in the successful design.

Here are a few design questions to help you out:

-
What information should be used on the page?
Ive provided a document which outlines all the information needed to put on homepage (attached to the brief - called brightwell_page_info). Also see the Must Have section below on this brief.

-
What links should appear in the navigation/footer?:
The navigation should provide links to the following pages (NOTE: services link has subcategories):
1 Homepage
2 Services
- Home loans
- Investment loans
- Refinancing loans
- Business loans
3 About Us
4 FAQ
5 Contact Us

-
What colors should be used in the design?
Our company colors - Cyan: #2EADE3, Blue: #004B70, White. Feel free to submit designs with slight variations if you feel it improves the design.

-
What should the layout of the page be?
This is up to you to come up with - we are open to different layouts for the page design (as long as they capture the information effectively and making it easy to understand).

Target Market(s)

Potential Home owners, Families and Business Owners

Industry/Entity Type

Business

Requirements
Must have
• - Must contain our logo (attached as PNG and Illustrator file)
- Winning designer must supply a Photoshop file (PSD) that will allow us.
Nice to have
• - Should include photos/images of families, professional groups, tradespeople etc (you can use stock photos from PixQuarry and I will purchase them once you are selected as the winning design)
- Link to a loan calculator somewhere on front page with a button 'Find out how much you could borrow' (or maybe even try adding a loan calculator to the homepage if you think this would look good)
- Page should have a main headline "Finding the right loan for you" or "Brightwell Lending finds the right loan for our customers."
- Must include Accreditation logos somewhere on the homepage (will try and supply these soon)
Should not have
• - Poor quality designs will not be considered
- Do not use clipart

```html
<!DOCTYPE html>
<html lang="en">
<head>
<meta charset="utf-8">
<title>Brightwell Lending – Finding the right loan for you</title>
<link href="https://fonts.googleapis.com/css2?family=Oswald:wght@300;400&family=Open+Sans:wght@400;600;700&display=swap" rel="stylesheet">
<style>
  :root {
    --cyan: #2eade3;
    --blue: #004b70;
    --navy-text: #1f4b66;
    --text: #444b50;
    --muted: #8a9198;
    --rule: #e3e6e8;
    --page-bg: #eef3f6;
    --white: #ffffff;
    --button-border: #c9cdd0;
    --badge: #b9bdc0;
  }
  * { box-sizing: border-box; margin: 0; padding: 0; }
  html, body { width: 929px; height: 1200px; overflow: hidden; }
  body { background: var(--page-bg); font-family: "Open Sans", Arial, sans-serif; color: var(--text); font-size: 11px; }
  a { text-decoration: none; color: inherit; }
  ul { list-style: none; }

  .page { position: absolute; left: 126px; top: 0; width: 666px; height: 1200px; background: var(--white); }
  .page > * { position: absolute; }

  .brand { left: 13px; top: 34px; display: flex; align-items: center; gap: 8px; }
  .brand-dot { width: 18px; height: 18px; border-radius: 50%; background: var(--cyan); }
  .brand-name { font-size: 19px; font-weight: 600; color: var(--blue); letter-spacing: -0.3px; }

  .main-nav { left: 13px; top: 105px; display: flex; gap: 0; font-size: 10px; color: var(--muted); }
  .main-nav > li { position: relative; padding: 0 9px 7px; }
  .main-nav > li:first-child { padding-left: 0; color: var(--blue); }
  .main-nav .is-open { color: var(--muted); border-bottom: 2px solid var(--cyan); }
  .submenu { position: absolute; left: 0; top: 21px; width: 96px; background: var(--white); padding: 2px 8px 4px; box-shadow: 0 2px 4px rgba(0,0,0,0.12); z-index: 2; }
  .submenu li { color: var(--cyan); padding: 4px 0 5px; border-bottom: 1px solid var(--rule); font-size: 10px; }
  .submenu li:last-child { border-bottom: 0; }

  .search { left: 472px; top: 104px; width: 179px; height: 19px; border: 1px solid var(--rule); display: flex; align-items: center; justify-content: space-between; padding: 0 6px; font-size: 9px; font-style: italic; color: #c2c6c9; }

  .hero { left: 13px; top: 138px; width: 638px; height: 304px; background: linear-gradient(160deg, #9cc5e4 0%, #d8c98a 35%, #8a9a6a 60%, #4f7a3b 100%); }
  .hero-caption { position: absolute; left: 257px; top: 160px; width: 381px; height: 87px; background: rgba(46,173,227,0.92); color: var(--white); font-size: 23px; display: flex; align-items: center; padding-left: 32px; }
  .slider-dots { left: 287px; top: 453px; display: flex; gap: 3px; }
  .slider-dots span { width: 9px; height: 9px; border-radius: 50%; border: 1px solid #d6d9db; background: var(--white); }
  .slider-dots span.active { background: #d6d9db; }

  .headline { left: 12px; top: 490px; font-family: "Oswald", sans-serif; font-weight: 300; font-size: 25px; color: var(--cyan); letter-spacing: -0.3px; }

  .services { left: 13px; top: 546px; display: flex; }
  .service { width: 163px; }
  .service h3 { font-family: "Oswald", sans-serif; font-weight: 300; font-size: 21px; color: var(--navy-text); margin-bottom: 8px; letter-spacing: -0.2px; }
  .service li { position: relative; padding-left: 18px; margin-bottom: 9px; line-height: 14px; width: 140px; font-size: 10px; }
  .service li svg { position: absolute; left: 0; top: 3px; }
  .btn { display: inline-block; margin-top: 7px; border: 1px solid var(--button-border); border-radius: 2px; padding: 3px 8px; font-size: 10px; color: #333; background: linear-gradient(#fff, #f2f3f4); }

  .divider { left: 13px; width: 638px; height: 1px; background: var(--rule); }

  .section-title { font-family: "Oswald", sans-serif; font-weight: 300; font-size: 25px; color: var(--cyan); letter-spacing: -0.3px; }

  .about { left: 13px; top: 750px; width: 340px; }
  .about .section-title { margin-bottom: 18px; }
  .about-photo { float: left; width: 149px; height: 99px; margin: 0 14px 4px 0; background: linear-gradient(135deg, #e7d3c3 0%, #f2f2f0 45%, #b9c4cc 100%); }
  .about p { font-size: 10px; line-height: 14.4px; margin-bottom: 14px; }
  .about .contact-line { font-weight: 700; color: #333; }

  .calculator { left: 391px; top: 750px; width: 260px; }
  .calculator .section-title { margin-bottom: 18px; }
  .calculator p { font-size: 10px; line-height: 14.4px; margin-bottom: 10px; }
  .calculator .btn { margin-top: 0; }
  .accreditations { display: flex; flex-wrap: wrap; gap: 10px 18px; width: 210px; margin-top: 28px; }
  .badge { background: var(--badge); }
  .badge.round { width: 50px; height: 70px; border-radius: 25px 25px 6px 6px; }
  .badge.square { width: 50px; height: 82px; }
  .badge.crest { width: 52px; height: 62px; border-radius: 26px 26px 4px 4px; }
  .badge.tile { width: 66px; height: 56px; margin-left: 14px; }
  .badge.wide { width: 96px; height: 48px; border-radius: 4px; }

  .site-footer { left: 13px; top: 1125px; width: 638px; height: 75px; border-top: 1px solid var(--rule); display: flex; justify-content: space-between; align-items: flex-start; padding-top: 29px; font-size: 10px; }
  .site-footer .link { color: var(--cyan); }
  .footer-nav { display: flex; gap: 18px; color: var(--cyan); }
  .footer-nav li:first-child { color: #333; }
</style>
</head>
<body>
<div class="page">
  <a class="brand" href="#"><span class="brand-dot"></span><span class="brand-name">Brightwell Lending</span></a>

  <ul class="main-nav">
    <li>Home</li>
    <li class="is-open">Services
      <ul class="submenu">
        <li>Home loans</li>
        <li>Investment loans</li>
        <li>Refinancing loans</li>
        <li>Business loans</li>
      </ul>
    </li>
    <li>About Us</li>
    <li>FAQ</li>
    <li>Contact Us</li>
  </ul>

  <div class="search"><span>Enter keywords</span>
    <svg width="9" height="9" viewBox="0 0 10 10"><circle cx="4" cy="4" r="3" fill="none" stroke="#c2c6c9" stroke-width="1.4"/><line x1="6.2" y1="6.2" x2="9.3" y2="9.3" stroke="#c2c6c9" stroke-width="1.6"/></svg>
  </div>

  <div class="hero" role="img" aria-label="Photo of a smiling young family with a baby in front of their new house">
    <div class="hero-caption">Finding the right loan for you</div>
  </div>
  <div class="slider-dots"><span class="active"></span><span></span><span></span><span></span><span></span></div>

  <h1 class="headline">We offer a unique approach to help you find the right:</h1>

  <div class="services">
    <div class="service">
      <h3>Home Loan</h3>
      <ul>
        <li><svg width="11" height="8" viewBox="0 0 11 8"><path d="M0 4h9M6 1l3 3-3 3" fill="none" stroke="#c7cbce" stroke-width="1.3"/></svg>Home buyers</li>
        <li><svg width="11" height="8" viewBox="0 0 11 8"><path d="M0 4h9M6 1l3 3-3 3" fill="none" stroke="#c7cbce" stroke-width="1.3"/></svg>First home buyers</li>
        <li><svg width="11" height="8" viewBox="0 0 11 8"><path d="M0 4h9M6 1l3 3-3 3" fill="none" stroke="#c7cbce" stroke-width="1.3"/></svg>Over 20 lenders</li>
      </ul>
      <a class="btn" href="#">Find Out More</a>
    </div>
    <div class="service">
      <h3>Investment Loan</h3>
      <ul>
        <li><svg width="11" height="8" viewBox="0 0 11 8"><path d="M0 4h9M6 1l3 3-3 3" fill="none" stroke="#c7cbce" stroke-width="1.3"/></svg>Property investment loans</li>
        <li><svg width="11" height="8" viewBox="0 0 11 8"><path d="M0 4h9M6 1l3 3-3 3" fill="none" stroke="#c7cbce" stroke-width="1.3"/></svg>Interest only loans</li>
      </ul>
      <a class="btn" href="#">Find Out More</a>
    </div>
    <div class="service">
      <h3>Refinancing</h3>
      <ul>
        <li><svg width="11" height="8" viewBox="0 0 11 8"><path d="M0 4h9M6 1l3 3-3 3" fill="none" stroke="#c7cbce" stroke-width="1.3"/></svg>Refinancing for the best rate</li>
        <li><svg width="11" height="8" viewBox="0 0 11 8"><path d="M0 4h9M6 1l3 3-3 3" fill="none" stroke="#c7cbce" stroke-width="1.3"/></svg>Upsizing or downsizing</li>
        <li><svg width="11" height="8" viewBox="0 0 11 8"><path d="M0 4h9M6 1l3 3-3 3" fill="none" stroke="#c7cbce" stroke-width="1.3"/></svg>Change from a variable to a fixed rate</li>
      </ul>
      <a class="btn" href="#">Find Out More</a>
    </div>
    <div class="service">
      <h3>Business Loan</h3>
      <ul>
        <li><svg width="11" height="8" viewBox="0 0 11 8"><path d="M0 4h9M6 1l3 3-3 3" fill="none" stroke="#c7cbce" stroke-width="1.3"/></svg>Long term</li>
        <li><svg width="11" height="8" viewBox="0 0 11 8"><path d="M0 4h9M6 1l3 3-3 3" fill="none" stroke="#c7cbce" stroke-width="1.3"/></svg>Short term</li>
        <li><svg width="11" height="8" viewBox="0 0 11 8"><path d="M0 4h9M6 1l3 3-3 3" fill="none" stroke="#c7cbce" stroke-width="1.3"/></svg>Equiptment and Leasing</li>
      </ul>
      <a class="btn" href="#">Find Out More</a>
    </div>
  </div>

  <div class="divider" style="top:724px"></div>

  <section class="about">
    <h2 class="section-title">About Brightwell Lending</h2>
    <div class="about-photo" role="img" aria-label="Photo of a finance adviser meeting with clients at a desk"></div>
    <p>At Brightwell Lending we work hard to find the right loan for our customers. We do that because we are backed by sound industry knowledge, professional experience and a great customer service approach.</p>
    <p>Brightwell Lending guarantees that we will always tailor the best solution for your individual lending needs.</p>
    <p>We can do that because we have access to a wide variety of lending options from major banks to non-bank lenders and we are committed to finding the right lending product for you.</p>
    <p>There are many different loan products in the marketplace. Brightwell Lending has access to a wide panel of lenders which means we can access bank and non-bank lenders that meet the individual needs of our customers.</p>
    <p class="contact-line">Contact Brightwell Lending today on: 1800 555 210 to find out more.</p>
  </section>

  <section class="calculator">
    <h2 class="section-title">Loan calculator</h2>
    <p>Lorem Ipsum is simply dummy text of the printing and typesetting industry. Lorem Ipsum has been the industry's standard dummy text ever since the 1500s.</p>
    <a class="btn" href="#">Use Calculator</a>
    <div class="accreditations" aria-label="Accreditations">
      <span class="badge round"></span>
      <span class="badge square"></span>
      <span class="badge crest"></span>
      <span class="badge tile"></span>
      <span class="badge wide"></span>
    </div>
  </section>

  <footer class="site-footer">
    <div>Brightwell Lending © 2012 | <a class="link" href="#">Privacy Policy</a></div>
    <ul class="footer-nav">
      <li>Home</li><li>Services</li><li>About Us</li><li>FAQ</li><li>Contact Us</li>
    </ul>
  </footer>
</div>
</body>
</html>
```